依頼詳細
アルコール除菌ジェルのラベルのデザインをお願い致します
サイズはW110mm×H154mm
ラミネート貼り
希望イメージ
シンプル 複雑
単色 カラフル
暗い 明るい
日常 高級
遊び心 厳粛
未来的 伝統的
女性的 男性的
希望する色
緑系
納品ファイル
• イラストレーター形式 (.ai)
補足説明
実際の現在のデザイン(他社)を添付致します。
添付のデザインのOEM製品になり弊社自社品となります
雰囲気を全然違うようにしてください
業務用です
添付の画像にありますKAVELは必要ございません
また発売元は弊社で製造元は別な会社で記載頂くと思います
宜しくお願い致します
容器の画像を添付致しました。
円形のPETボトルになります
販売先は自動車ディーラー様中心となります
■ 選んだ理由

ディーラー様及び通常の販売先において頂けるデザインでした
関係者で3点選びましたが、全員がこの方のデザインが上がりましたので
決定しました

■ 提案者全員のお礼・コメント

沢山の方からデザインをあげて頂き非常に迷いました。
今後もこのサイトを使って新商品のデザインや
容器のデザインをお願いしたいと思いますのでその際は
宜しいお願い致します。今回はありがとうございました

```html
<!DOCTYPE html>
<html lang="ja">
<head>
<meta charset="utf-8">
<title>アルコール除菌ジェル ラベル</title>
<link rel="stylesheet" href="https://fonts.googleapis.com/css2?family=M+PLUS+1p:wght@500;800&family=Noto+Sans+JP:wght@400;700&display=swap">
<style>
:root{
  --paper:#ffffff;
  --blue:#2b4ea1;
  --pink:#ec5f7c;
  --pink-deep:#e2456a;
  --ink:#222222;
  --crop:#555555;
  --white:#ffffff;
}
*{box-sizing:border-box;margin:0;padding:0}
html,body{width:893px;height:1200px;overflow:hidden;background:var(--paper)}
body{position:relative;font-family:"Noto Sans JP",sans-serif;color:var(--ink)}
.crop-marks{position:absolute;inset:0}
.front-panel{position:absolute;left:105px;top:118px;width:694px;height:518px;background:var(--blue);border-radius:26px;overflow:hidden}
.stop-mark{position:absolute;left:197px;top:34px;width:300px;height:300px;border-radius:50%;background:var(--pink)}
.product-title{position:absolute;left:0;right:0;text-align:center;color:var(--white);font-family:"M PLUS 1p",sans-serif;font-weight:800;line-height:1}
.product-title.sub{top:165px;font-size:92px;letter-spacing:2px}
.product-title.main{top:300px;font-size:128px;letter-spacing:4px}
.info-panel{position:absolute;left:105px;top:664px;width:694px;height:456px;background:var(--pink);border-radius:22px;padding:22px 24px}
.badge-row{display:flex;gap:10px;align-items:center}
.volume{background:var(--white);border:2px solid var(--pink-deep);font-weight:700;font-size:22px;padding:0 10px;line-height:30px}
.fire-warning{background:var(--white);color:var(--pink-deep);font-weight:700;font-size:22px;padding:0 12px;line-height:30px}
.badge-note{color:var(--white);font-size:11px}
.spec-table{width:100%;margin-top:10px;border-collapse:collapse;background:var(--white);font-size:11px}
.spec-table td{border:1px solid var(--pink-deep);padding:3px 6px;line-height:1.35}
.spec-table .label{width:60px;text-align:center;font-weight:700;background:#fde6eb}
.notes{margin-top:10px;background:var(--white);padding:8px 10px;font-size:10px;line-height:1.5}
.notes h3{font-size:11px;font-weight:700}
.company{margin-top:10px;background:var(--white);padding:8px 10px;font-size:10px;line-height:1.5;display:flex;justify-content:space-between;align-items:flex-end}
.seller-name{display:flex;align-items:center;gap:6px;font-weight:700;font-size:13px}
.seller-name .dot{width:12px;height:12px;background:var(--pink-deep)}
.marks{display:flex;gap:8px}
.marks span{width:40px;height:40px;border:2px solid var(--ink);border-radius:50%}
.marks span.square{border-radius:4px}
</style>
</head>
<body>
<svg class="crop-marks" width="893" height="1200" aria-hidden="true">
  <g stroke="var(--crop)" stroke-width="1" fill="none">
    <path d="M20 105H90M105 20V95M873 105H813M788 20V95"/>
    <path d="M20 1135H90M105 1180V1145M873 1135H813M788 1180V1145"/>
    <path d="M20 650H80M813 650H873"/>
  </g>
</svg>

<section class="front-panel">
  <div class="stop-mark" role="img" aria-label="手のひらを向けた禁止マークのイラスト"></div>
  <p class="product-title sub">アルコール</p>
  <p class="product-title main">除菌ジェル</p>
</section>

<section class="info-panel">
  <div class="badge-row">
    <span class="volume">1L</span>
    <span class="fire-warning">火気厳禁</span>
    <span class="badge-note">第四類 アルコール類</span>
  </div>
  <table class="spec-table">
    <tr><td class="label">品名</td><td>アルコール除菌ジェル</td><td class="label">用途</td><td>手指の衛生・除菌に</td></tr>
    <tr><td class="label">成分</td><td>エタノール(濃度65〜70vol%)、水</td><td class="label">使用量</td><td>適量を手に取りよくすり込む</td></tr>
    <tr><td class="label">添加物</td><td>グリセリン、カルボマー、TEA</td><td class="label">保管</td><td>直射日光を避け冷暗所で保管</td></tr>
  </table>
  <div class="notes">
    <h3>使用上の注意</h3>
    <p>目に入らないよう注意し、入った場合はすぐに水で十分に洗い流してください。傷や湿疹など異常のある部位には使用しないでください。肌に合わない場合は使用を中止し、医師に相談してください。火気の近くで使用しないでください。</p>
    <h3>保管上の注意</h3>
    <p>高温になる場所や車内に放置しないでください。乳幼児の手の届かない所に保管してください。使用後はキャップをしっかり閉めてください。</p>
  </div>
  <div class="company">
    <div>
      <p class="seller-name"><span class="dot"></span>発売元 株式会社ミナトケア</p>
      <p>〒100-0000 東京都千代田区架空町1-2-3 TEL 03-0000-0000</p>
      <p>製造元 株式会社アオバ化成</p>
      <p>〒500-0000 岐阜県架空市中央4-5-6 TEL 058-000-0000</p>
    </div>
    <div class="marks"><span></span><span class="square"></span></div>
  </div>
</section>
</body>
</html>
```